Brookmere Osteopathy flyer

I want a clean clear DL flyer (but also want an A4 poster) promoting a new Osteopathic business in a semi rural area in Tasmania (Australia).
It can have pictures like the examples attached to show people what Osteopathy is (its like Chiropractic and physiotherapy).
I am the sole practioner and am male, so any pictures would be best to be a white male if possible.
I've attached some wording, you can use all, or none of it
I don't have a phone number for the business yet
info@brookmereosteopathy.example
www.brookmereosteopathy.example
Target Market(s)
Australians, from tradies, professionals, babies to retired people
Industry/Entity Type
Health
Look and feel

```html
<!DOCTYPE html>
<html lang="en">
<head>
<meta charset="utf-8">
<title>Brookmere Osteopathy – DL Flyer</title>
<link href="https://fonts.googleapis.com/css2?family=Oswald:wght@500;600&family=Poppins:wght@400;500;600&display=swap" rel="stylesheet">
<style>
  :root {
    --blue: #1a8fce;
    --blue-deep: #0f7fc0;
    --orange: #e8892f;
    --ink: #2b2b2b;
    --paper: #ffffff;
    --backdrop: #d9d8dc;
    --photo-light: #c9d3de;
    --photo-mid: #9aa6b4;
  }
  * { box-sizing: border-box; margin: 0; padding: 0; }
  html, body { width: 704px; height: 1200px; overflow: hidden; }
  body {
    background: var(--backdrop);
    font-family: "Poppins", sans-serif;
    color: var(--ink);
    position: relative;
  }
  .flyer {
    position: absolute;
    top: 250px;
    width: 330px;
    height: 700px;
    background: var(--paper);
    overflow: hidden;
  }
  .flyer--front { left: 16px; }
  .flyer--back { left: 358px; }

  .photo {
    position: absolute;
    left: 0; width: 100%;
  }
  .flyer--front .photo {
    top: 50px; height: 290px;
    background: linear-gradient(160deg, var(--photo-light) 0%, #b8c2cf 40%, var(--photo-mid) 75%, #e6e9ee 100%);
  }
  .flyer--back .photo {
    top: 0; height: 245px;
    background: linear-gradient(150deg, #eeeeee 0%, #c8b8a8 35%, #4f5a78 65%, #d4c0ac 100%);
  }
  .wave {
    position: absolute;
    left: 0; width: 330px;
  }

  .brand {
    position: absolute;
    top: 8px; left: 0; width: 100%;
    display: flex; align-items: center; justify-content: center; gap: 6px;
    z-index: 2;
  }
  .brand__dot {
    width: 12px; height: 12px; border-radius: 50%;
    background: var(--orange);
  }
  .brand__name {
    font-family: "Poppins", sans-serif;
    font-weight: 600;
    font-size: 13px;
    color: var(--blue);
  }

  .headline {
    position: absolute;
    left: 31px; top: 340px;
    font-family: "Oswald", sans-serif;
    font-weight: 600;
    font-size: 36px;
    line-height: 43px;
    text-transform: uppercase;
    letter-spacing: 0.3px;
  }
  .headline span { display: block; color: var(--blue); }
  .headline span.accent { color: var(--orange); }

  .intro {
    position: absolute;
    left: 32px; top: 475px; width: 270px;
    font-size: 9.6px;
    line-height: 13px;
  }

  .section-title {
    position: absolute;
    top: 262px; left: 0; width: 100%;
    text-align: center;
    font-family: "Oswald", sans-serif;
    font-weight: 500;
    font-size: 23px;
    line-height: 31px;
    text-transform: uppercase;
  }
  .section-title span { display: block; color: var(--blue); }
  .section-title span.accent { color: var(--orange); }
  .section-rule {
    position: absolute;
    top: 333px; left: 124px;
    width: 81px; height: 2px;
    background: var(--orange);
  }

  .reasons {
    position: absolute;
    top: 367px; left: 28px;
    width: 290px;
    list-style: none;
    display: grid;
    grid-template-columns: 132px 158px;
    row-gap: 9px;
  }
  .reasons li {
    display: flex; align-items: center; gap: 7px;
    font-size: 9.6px; line-height: 11px;
    min-height: 27px;
  }
  .reasons__icon {
    flex: none;
    width: 26px; height: 26px; border-radius: 50%;
    background: var(--blue);
    display: flex; align-items: center; justify-content: center;
  }

  .call-icon {
    position: absolute;
    width: 30px; height: 30px; border-radius: 50%;
    background: var(--blue);
    border: 2px solid var(--paper);
    display: flex; align-items: center; justify-content: center;
    z-index: 2;
  }
  .contact-pill {
    position: absolute;
    left: 26px; width: 267px; height: 57px;
    background: var(--orange);
    border-radius: 16px;
    color: var(--paper);
    text-align: center;
    padding-top: 10px;
  }
  .contact-pill__phone {
    font-weight: 600;
    font-size: 19px;
    letter-spacing: 2px;
    line-height: 24px;
  }
  .contact-pill__address {
    font-size: 8px;
    line-height: 12px;
  }
  .flyer--front .call-icon { left: 142px; top: 566px; }
  .flyer--front .contact-pill { top: 586px; }
  .flyer--back .call-icon { left: 149px; top: 570px; }
  .flyer--back .contact-pill { top: 587px; }

  .links {
    position: absolute;
    left: 0; width: 100%;
    display: flex; justify-content: center; gap: 10px;
    font-size: 8.2px;
  }
  .flyer--front .links { top: 650px; }
  .flyer--back .links { top: 660px; }

  .footer-band {
    position: absolute;
    left: 0; bottom: 0; width: 100%; height: 20px;
    background: var(--blue-deep);
  }
</style>
</head>
<body>

<section class="flyer flyer--front" aria-label="Flyer front">
  <div class="photo" role="img" aria-label="Photo of an osteopath gently treating a reclining patient's head and neck"></div>
  <svg class="wave" style="top:270px" width="330" height="80" viewBox="0 0 330 80" aria-hidden="true">
    <path d="M0,64 C60,44 110,70 180,50 S290,18 330,10 L330,80 L0,80 Z" fill="#ffffff"/>
    <path d="M4,62 C60,42 110,68 180,48 S290,16 330,8" fill="none" stroke="#1a8fce" stroke-width="14"/>
  </svg>

  <div class="brand">
    <span class="brand__dot"></span>
    <span class="brand__name">Brookmere Osteopathy</span>
  </div>

  <h1 class="headline">
    <span>Australia’s</span>
    <span>Best Osteopathy</span>
    <span class="accent">Clinic Service</span>
  </h1>

  <p class="intro">The osteopathic physician focuses on the joints, muscles, and spine. Osteopathic intervention can help treat arthritis, back pain, headaches, tennis elbow, digestive issues, and postural problems. Treatment can also assist with sleep cycles and the nervous, circulatory, and lymphatic symptoms.</p>

  <div class="call-icon">
    <svg width="14" height="14" viewBox="0 0 24 24" aria-hidden="true"><path fill="#fff" d="M6.6 10.8a15.1 15.1 0 0 0 6.6 6.6l2.2-2.2a1 1 0 0 1 1-.25 11.4 11.4 0 0 0 3.6.57 1 1 0 0 1 1 1V20a1 1 0 0 1-1 1A17 17 0 0 1 3 4a1 1 0 0 1 1-1h3.5a1 1 0 0 1 1 1c0 1.25.2 2.45.57 3.57a1 1 0 0 1-.25 1z"/></svg>
  </div>
  <div class="contact-pill">
    <div class="contact-pill__phone">555(0142)6620981</div>
    <div class="contact-pill__address">24 Millbrook Lane, Brookmere</div>
  </div>
  <div class="links">
    <span>www.brookmereosteopathy.example</span>
    <span>info@brookmereosteopathy.example</span>
  </div>
  <div class="footer-band"></div>
</section>

<section class="flyer flyer--back" aria-label="Flyer back">
  <div class="photo" role="img" aria-label="Photo of an osteopath's hands treating a patient's shoulder"></div>
  <svg class="wave" style="top:170px" width="330" height="80" viewBox="0 0 330 80" aria-hidden="true">
    <path d="M0,66 C50,40 100,72 170,54 S280,30 330,14 L330,80 L0,80 Z" fill="#ffffff"/>
    <path d="M4,64 C50,38 100,70 170,52 S280,28 330,12" fill="none" stroke="#1a8fce" stroke-width="14"/>
  </svg>

  <h2 class="section-title">
    <span>Common Reasons</span>
    <span class="accent">People Visit an Osteopath:</span>
  </h2>
  <div class="section-rule"></div>

  <ul class="reasons">
    <li><span class="reasons__icon"><svg width="10" height="10" viewBox="0 0 10 10" aria-hidden="true"><circle cx="5" cy="5" r="3" fill="#fff"/></svg></span>Back / neck pain</li>
    <li><span class="reasons__icon"><svg width="10" height="10" viewBox="0 0 10 10" aria-hidden="true"><circle cx="5" cy="5" r="3" fill="#fff"/></svg></span>Headaches / migraines</li>
    <li><span class="reasons__icon"><svg width="10" height="10" viewBox="0 0 10 10" aria-hidden="true"><circle cx="5" cy="5" r="3" fill="#fff"/></svg></span>Plantar fasciitis</li>
    <li><span class="reasons__icon"><svg width="10" height="10" viewBox="0 0 10 10" aria-hidden="true"><circle cx="5" cy="5" r="3" fill="#fff"/></svg></span>Joint and muscle pain</li>
    <li><span class="reasons__icon"><svg width="10" height="10" viewBox="0 0 10 10" aria-hidden="true"><circle cx="5" cy="5" r="3" fill="#fff"/></svg></span>Tennis / Golfers<br>elbow</li>
    <li><span class="reasons__icon"><svg width="10" height="10" viewBox="0 0 10 10" aria-hidden="true"><circle cx="5" cy="5" r="3" fill="#fff"/></svg></span>Disc related issues</li>
    <li><span class="reasons__icon"><svg width="10" height="10" viewBox="0 0 10 10" aria-hidden="true"><circle cx="5" cy="5" r="3" fill="#fff"/></svg></span>Tendonitis / Bursitis</li>
    <li><span class="reasons__icon"><svg width="10" height="10" viewBox="0 0 10 10" aria-hidden="true"><circle cx="5" cy="5" r="3" fill="#fff"/></svg></span>Sciatica</li>
    <li><span class="reasons__icon"><svg width="10" height="10" viewBox="0 0 10 10" aria-hidden="true"><circle cx="5" cy="5" r="3" fill="#fff"/></svg></span>Adhesive capsulitis<br>(frozen shoulder)</li>
    <li><span class="reasons__icon"><svg width="10" height="10" viewBox="0 0 10 10" aria-hidden="true"><circle cx="5" cy="5" r="3" fill="#fff"/></svg></span>Pregnancy-related<br>discomfort</li>
  </ul>

  <div class="call-icon">
    <svg width="14" height="14" viewBox="0 0 24 24" aria-hidden="true"><path fill="#fff" d="M6.6 10.8a15.1 15.1 0 0 0 6.6 6.6l2.2-2.2a1 1 0 0 1 1-.25 11.4 11.4 0 0 0 3.6.57 1 1 0 0 1 1 1V20a1 1 0 0 1-1 1A17 17 0 0 1 3 4a1 1 0 0 1 1-1h3.5a1 1 0 0 1 1 1c0 1.25.2 2.45.57 3.57a1 1 0 0 1-.25 1z"/></svg>
  </div>
  <div class="contact-pill">
    <div class="contact-pill__phone">555(0142)6620981</div>
    <div class="contact-pill__address">24 Millbrook Lane, Brookmere</div>
  </div>
  <div class="links">
    <span>www.brookmereosteopathy.example</span>
    <span>info@brookmereosteopathy.example</span>
  </div>
  <div class="footer-band"></div>
</section>

</body>
</html>
```